Business Card Design Graduates

Slogan
"Practical Skills + Theory = Paid Job"

We assist Accounting Graduates to get work at the end of their University Degree by offering them a 6 week practical experience program.

At completion of the program they get business cards in their own Name, Title, phone numbers, address and email address. So, I need to be able to have a template where I can change these details and purchase business cards via Cardlomo or other outside printers.

I want it to be a bit colourful... ie not a plain white background or black, some blue would be nice. But it also needs to look professional as they will be meeting with future employers and networking. We help them get a paid job in Accounting at completion of the 6 week program.

Target Market(s)

Students and Employers

Industry/Entity Type

Business

Contact Information for Business Card

Marietta Kolopenakis, Director, PO Box 418, Brindlewood NSW 2190, Phone: 9412-5073 Fax: 9412-8291 Email: mariettak@torvinhq.com.au Web: www.TorvinWorkBridge.com.au

Requirements
Must have
• changeable fields for me to change details for each student who graduates. The name of the company is already in the logo so no need to duplicate the name. Look at the website www.TorvinWorkBridge.com.au because we expect the design should match our Corporate Image.

```html
<!DOCTYPE html>
<html lang="en">
<head>
<meta charset="utf-8">
<title>Torvin WorkBridge – Business Card</title>
<link rel="stylesheet" href="https://fonts.googleapis.com/css2?family=Open+Sans:wght@400;600&display=swap">
<style>
  :root {
    --page: #e8e5e0;
    --blue-deep: #0b4f9e;
    --blue-mid: #1f6fcc;
    --blue-light: #3a8ee0;
    --green: #9acd32;
    --white: #ffffff;
    --ink-blue: #1d62b8;
    --grey: #6b7280;
  }
  html, body {
    margin: 0;
    width: 704px;
    height: 1200px;
    overflow: hidden;
    background: var(--page);
    font-family: "Open Sans", Arial, sans-serif;
  }
  .canvas {
    position: relative;
    width: 704px;
    height: 1200px;
  }
  .card {
    position: absolute;
    left: 72px;
    width: 560px;
    height: 340px;
    border-radius: 16px;
    overflow: hidden;
    box-shadow: 0 6px 18px rgba(0,0,0,.18);
  }

  /* Front */
  .card-front {
    top: 140px;
    background: linear-gradient(160deg, var(--blue-light) 0%, var(--blue-mid) 45%, var(--blue-deep) 100%);
  }
  .front-brand {
    position: absolute;
    left: 0; right: 0;
    top: 128px;
    text-align: center;
    color: var(--white);
  }
  .brand-mark {
    display: inline-flex;
    align-items: center;
    gap: 12px;
    font-weight: 400;
    font-size: 46px;
    letter-spacing: .5px;
  }
  .brand-dot {
    width: 22px; height: 22px;
    border-radius: 50%;
    background: var(--green);
  }
  .front-url {
    margin-top: 10px;
    font-size: 17px;
    font-weight: 600;
  }

  /* Back */
  .card-back {
    top: 720px;
    background: var(--white);
  }
  .back-photo {
    position: absolute;
    right: 0; top: 0;
    width: 290px; height: 205px;
    background: linear-gradient(120deg, #f4f5f7 0%, #d9dde3 40%, #b9c3cf 70%, #e6e9ed 100%);
  }
  .back-band {
    position: absolute;
    left: 0; top: 0;
  }
  .back-brand {
    position: absolute;
    left: 26px; top: 112px;
    color: var(--ink-blue);
  }
  .back-brand .brand-mark { font-size: 30px; gap: 8px; }
  .back-brand .brand-dot { width: 14px; height: 14px; }
  .holder {
    position: absolute;
    left: 26px; top: 168px;
  }
  .holder-name {
    margin: 0;
    font-size: 17px;
    font-weight: 600;
    color: var(--ink-blue);
  }
  .holder-title {
    margin: 2px 0 0;
    font-size: 12px;
    color: var(--grey);
  }
  .address {
    position: absolute;
    left: 26px; bottom: 30px;
    margin: 0;
    font-size: 13px;
    color: var(--white);
  }
  .contact {
    position: absolute;
    right: 26px; top: 226px;
    margin: 0; padding: 0;
    list-style: none;
    color: var(--white);
    font-size: 13px;
    line-height: 21px;
    text-align: right;
  }
  .contact li {
    display: flex;
    justify-content: flex-end;
    align-items: center;
    gap: 8px;
  }
  .contact-label {
    display: inline-block;
    width: 16px;
    font-size: 11px;
    color: var(--green);
    text-align: center;
  }
  .contact svg { width: 12px; height: 12px; }
</style>
</head>
<body>
<main class="canvas">

  <section class="card card-front" aria-label="Card front">
    <div class="front-brand">
      <div class="brand-mark"><span class="brand-dot"></span>Torvin WorkBridge</div>
      <div class="front-url">www.TorvinWorkBridge.com.au</div>
    </div>
  </section>

  <section class="card card-back" aria-label="Card back">
    <div class="back-photo" role="img" aria-label="Photograph of smiling graduate students holding folders"></div>

    <svg class="back-band" width="560" height="340" viewBox="0 0 560 340" aria-hidden="true">
      <defs>
        <linearGradient id="bandBlue" x1="0" y1="0" x2="1" y2="1">
          <stop offset="0" stop-color="#2a7fd6"/>
          <stop offset="1" stop-color="#0b4f9e"/>
        </linearGradient>
      </defs>
      <polygon points="0,262 560,205 560,340 0,340" fill="url(#bandBlue)"/>
      <polygon points="0,256 560,199 560,207 0,264" fill="#9acd32"/>
    </svg>

    <div class="back-brand">
      <div class="brand-mark"><span class="brand-dot"></span>Torvin WorkBridge</div>
    </div>

    <div class="holder">
      <p class="holder-name">Marietta Kolopenakis</p>
      <p class="holder-title">Director</p>
    </div>

    <p class="address">PO Box 418, Brindlewood NSW 2190</p>

    <ul class="contact">
      <li>9412-5073
        <svg viewBox="0 0 12 12"><path d="M2 1h2l1 3-1.5 1a6 6 0 0 0 3.5 3.5L8 7l3 1v2a1 1 0 0 1-1 1A9 9 0 0 1 1 2a1 1 0 0 1 1-1z" fill="#9acd32"/></svg>
      </li>
      <li>9412-8291 <span class="contact-label">Fx</span></li>
      <li>mariettak@torvinhq.com.au
        <svg viewBox="0 0 12 12"><rect x="1" y="2.5" width="10" height="7" rx="1" fill="#9acd32"/><path d="M1.5 3l4.5 3.5L10.5 3" stroke="#0b4f9e" fill="none"/></svg>
      </li>
      <li>www.TorvinWorkBridge.com.au
        <svg viewBox="0 0 12 12"><circle cx="6" cy="6" r="5" fill="none" stroke="#9acd32" stroke-width="1.3"/><path d="M1 6h10M6 1c-2.5 3-2.5 7 0 10M6 1c2.5 3 2.5 7 0 10" stroke="#9acd32" fill="none"/></svg>
      </li>
    </ul>
  </section>

</main>
</body>
</html>
```